Web Design for couples website

About us:
Duoglimmer.sg is a new startup website that aims to suggest and promote activities for young couples. The site will feature a blog and a group deals page (i.e Bulkaro).

What we need:
We require a talented designer to design a theme for the website. The design must include at least the following:
1. Logo Design - A logo should be provided along with the website design. The design should match the overall design of the website (or vice versa). The logo should include the words "Duoglimmer.sg" or "Duoglimmer". Capitalisation of the alphabets are not critical.

2 - Home / Landing page
The layout of this page should be similar to the standard 2 / 3 column quillpress pages with an image slider on top to feature articles / deals. There should also be a column on the side to include widgets such as social networking and mailing list subscription, etc

3. Deals Listing Page
This page will have a listing of all current group deals, similar to that of Bulkaro. The layout can either have deals listed in 1 or 2 columns.

4. Past Deals Page - See references below

5. Deal Page
Detailed information page for each specific deal. This should include deal image, title, buy button, timer, social media buttons, two column text.

References for deal pages:
www.ventopik.com.sg
http://www.plumvoucher.com.au/daily-offers
www.tarnibuyasia.com
www.frolmart.com

6. General page design for miscellaneous pages like "About", "Contact", etc.

The overall theme of the website should cater to an audience of 18-30 year old young adults. Preferably to have something less colourful and give the overall feel of class. This should cater generally to females but males as well, so less (or no)pink / red would be preferable. But don't let yourself get restricted by these requirements and feel free to let your creative juices flow!
Updates

Hi Designers,

Thank you for your submissions so far. I would like to point out that the deal listing page will only be a sub section of the page.  Would appreciate if priority was given to the main / landing page slider and 2 or 3 columns for articles below.

Other priority would be for the single deal design, where I'm more interested to have more unique buttons such as "buy now" and "time left" .

Also to note, only .PSD design file is required. No coding (HTML / CSS) is necessary and should also be friendly for developers to work with.

Hi Designers,

 
Please submit proposal designs based on requirements on landing page or deal listings page as these would be my main requirements for consideration.

Also, Do try to keep the theme clean and easy on the eyes. Overall, I'm looking for something that is simplistic and/or classy with elegance.

Target Market(s)

18 - 30 years old young adults interested in dating and activities for couples

Industry/Entity Type

Media

Requirements
Must have
• - Logo
- Home
- Deal Page (specific)
- General layout

```html
<!DOCTYPE html>
<html lang="en">
<head>
<meta charset="utf-8">
<title>Duoglimmer – Deals</title>
<link rel="stylesheet" href="https://fonts.googleapis.com/css2?family=Questrial&family=Open+Sans:wght@400;600&family=Oswald:wght@500&display=swap">
<style>
:root{
  --bg:#4a4545;
  --header:#2e2a2a;
  --nav:#1d1a1a;
  --panel:#2d2929;
  --panel-2:#343030;
  --results:#5d5656;
  --card:#4a4444;
  --card-line:#6e6666;
  --green:#a7c83d;
  --green-dark:#86a62a;
  --red:#b3292a;
  --crimson:#8c1131;
  --ink:#2a2626;
  --text:#e9e4e0;
  --muted:#c9c2bd;
  --field:#eeeae5;
  --band:#7a7272;
  --footer:#3e3939;
  --bottom:#1e1b1b;
}
*{box-sizing:border-box;margin:0;padding:0}
html,body{width:811px;height:1200px;overflow:hidden}
body{position:relative;background:radial-gradient(ellipse at 40% 30%,#5a5454 0%,var(--bg) 60%,#3f3a3a 100%);font-family:"Questrial",sans-serif;color:var(--text)}
.abs{position:absolute}
.site-header{position:absolute;left:0;top:0;width:811px;height:123px;background:linear-gradient(160deg,#3a3535 0%,var(--header) 55%,#252121 100%)}
.logo{left:36px;top:36px;font-size:40px;color:var(--green);letter-spacing:-1px}
.lang-label{left:639px;top:51px;font-size:10px;color:var(--muted)}
.lang-select{left:714px;top:45px;width:59px;height:22px;background:#5a5555;border-radius:3px;font-size:10px;color:#ddd;padding:5px 0 0 8px}
.lang-select svg{position:absolute;right:6px;top:8px}
.mail-label{left:436px;top:92px;font-size:12.5px;color:#cfc8c3}
.mail-field{left:593px;top:87px;width:180px;height:25px;background:#d8c6c6;border:1px solid #eee}
.mail-btn{right:2px;top:2px;height:19px;padding:3px 4px;background:#111;color:var(--green);font-size:10.5px}
.main-nav{position:absolute;left:0;top:123px;width:811px;height:61px;background:var(--nav);display:flex;align-items:center;padding-left:36px;font-size:13px;color:#cfc9c5}
.main-nav span.sep{margin:0 13px;color:#8b8480}
.main-nav .active{color:var(--green)}
.search-panel{left:35px;top:212px;width:739px;height:115px;background:rgba(35,32,32,.75)}
.h-green{color:var(--green);font-size:15.5px}
.field{background:var(--field);height:25px;font-family:"Open Sans",sans-serif;font-style:italic;font-size:9px;color:#777;padding:7px 10px}
.go-btn{width:60px;height:24px;background:linear-gradient(#b3d64b,#93b92f);border-radius:2px;color:#1e2a10;font-size:12px;display:flex;align-items:center;justify-content:center;gap:8px}
.divider{left:289px;top:226px;width:1px;height:86px;background:#5a5555}
.small-label{font-size:9.5px;color:#ddd;font-family:"Open Sans",sans-serif}
.deals-panel{left:35px;top:350px;width:739px;height:537px;background:rgba(38,34,34,.7)}
.cat-list{left:53px;top:403px;list-style:none}
.cat-list li{height:31.2px;display:flex;align-items:flex-start;font-size:13px;color:#eee}
.cat-list .box{width:9px;height:9px;background:#eee;margin:3px 12px 0 1px;position:relative}
.count{right:26px;top:366px;font-size:11px;font-family:"Open Sans",sans-serif;color:#eee}
.count b{color:var(--green);font-weight:400}
.results{left:169px;top:395px;width:591px;height:478px;background:var(--results)}
.pointer{left:159px;top:434px;width:0;height:0;border-top:8px solid transparent;border-bottom:8px solid transparent;border-right:10px solid var(--results)}
.deal-card{position:absolute;left:177px;width:570px;height:146px;background:var(--card);border:1px solid var(--card-line)}
.deal-title{position:absolute;left:8px;top:8px;width:320px;font-family:"Open Sans",sans-serif;font-size:12.5px;line-height:15.5px;color:#fff}
.deal-photo{position:absolute;left:8px;top:51px;width:134px;height:78px;border:1px solid #ddd}
.deal-text{position:absolute;left:146px;top:54px;width:217px;font-family:"Open Sans",sans-serif;font-size:8.6px;line-height:12.5px;color:#eee;text-align:justify}
.deal-text a{color:#d8c15b;text-decoration:underline;float:right}
.deal-address{position:absolute;left:149px;top:101px;font-family:"Open Sans",sans-serif;font-size:8.6px;line-height:12.5px;color:#eee}
.deal-address b{font-weight:400;color:var(--green)}
.deal-address span{display:block;padding-left:39px}
.price-box{position:absolute;left:379px;top:7px;width:185px;height:127px;background:#fbfbfb;border:1px solid #ccc}
.price{position:absolute;left:15px;top:8px;font-family:"Oswald",sans-serif;font-size:24px;color:var(--red);white-space:nowrap}
.price em{font-style:normal;color:#8aa52a;font-size:17px}
.price-band{position:absolute;left:0;top:49px;width:100%;height:28px;background:linear-gradient(#e4e4e4,#d0d0d0);display:flex;align-items:center;justify-content:center;gap:6px;font-family:"Open Sans",sans-serif;font-size:9.5px;color:#222}
.price-band .days{font-family:"Questrial",sans-serif;font-size:16px;color:var(--red)}
.price-band .num{font-family:"Questrial",sans-serif;font-size:15px}
.price-band .unit{font-size:8px;margin-right:4px}
.btn-more{position:absolute;left:16px;top:92px;width:61px;height:21px;background:linear-gradient(#666,#222);color:#eee;font-size:10.5px;font-family:"Open Sans",sans-serif;text-align:center;line-height:21px;border-radius:2px}
.btn-buy{position:absolute;left:95px;top:91px;width:81px;height:23px;background:var(--crimson);color:#fff;font-size:11px;font-family:"Open Sans",sans-serif;text-align:center;line-height:23px;border-radius:2px}
.quick-links{left:0;top:903px;width:811px;height:50px;background:var(--band);font-family:"Open Sans",sans-serif;font-size:10.5px;color:#1c1a1a}
.quick-links span{position:absolute;top:19px}
.quick-links span::before{content:"";position:absolute;left:-10px;top:5px;width:4px;height:4px;border-radius:50%;background:#1c1a1a}
.site-footer{left:0;top:953px;width:811px;height:180px;background:var(--footer);font-family:"Open Sans",sans-serif;font-size:10px;color:#e8e3df}
.f-head{position:absolute;top:13px;font-size:10.5px;color:var(--green)}
.f-col{position:absolute;top:39px;list-style:none;line-height:18px}
.f-sep{left:517px;top:13px;width:1px;height:148px;background:#5c5656}
.bottom-bar{left:0;top:1133px;width:811px;height:67px;background:var(--bottom);font-family:"Open Sans",sans-serif;font-size:8.5px;color:#ddd}
.social{position:absolute;top:1156px;width:17px;height:17px;border-radius:2px}
</style>
</head>
<body>

<header class="site-header">
  <div class="abs logo">duoglimmer</div>
  <div class="abs lang-label">Select language :</div>
  <div class="abs lang-select">English
    <svg width="9" height="6" viewBox="0 0 9 6"><path d="M1 1l3.5 3.5L8 1" stroke="#ddd" stroke-width="1.4" fill="none"/></svg>
  </div>
  <div class="abs mail-label">Get the Daily Deals E - mail:</div>
  <div class="abs mail-field"><div class="abs mail-btn">Submit</div></div>
</header>

<nav class="main-nav">
  <span class="active">Home</span><span class="sep">|</span>
  <span>How it works</span><span class="sep">|</span>
  <span>Deal of the day</span><span class="sep">|</span>
  <span>Insta Deals</span><span class="sep">|</span>
  <span>Deal Zone</span><span class="sep">|</span>
  <span>Upcoming Deals</span><span class="sep">|</span>
  <span>Deals Map</span>
</nav>

<section class="abs search-panel"></section>
<div class="abs h-green" style="left:72px;top:223px">Search</div>
<div class="abs field" style="left:71px;top:249px;width:182px">search deals...</div>
<div class="abs go-btn" style="left:193px;top:286px">
  <svg width="14" height="14" viewBox="0 0 14 14"><circle cx="8.5" cy="5.5" r="4" fill="#eee" stroke="#555" stroke-width="1.4"/><path d="M5.5 8.5L1.5 12.5" stroke="#444" stroke-width="2.4"/></svg>Go</div>
<div class="abs divider"></div>
<div class="abs h-green" style="left:323px;top:223px">Deals Special Offers in a City</div>
<div class="abs field" style="left:322px;top:249px;width:110px">Country</div>
<div class="abs field" style="left:445px;top:249px;width:109px">City</div>
<div class="abs small-label" style="left:568px;top:256px">Deals From :</div>
<div class="abs field" style="left:624px;top:249px;width:109px">Restaurant
  <svg style="position:absolute;right:10px;top:10px" width="10" height="6" viewBox="0 0 10 6"><path d="M0 0h10L5 6z" fill="#666"/></svg></div>
<div class="abs" style="left:531px;top:289px;width:25px;height:20px;background:var(--field);font-size:10px;color:#555;text-align:center;line-height:20px">15</div>
<div class="abs small-label" style="left:562px;top:293px">Result per page</div>
<div class="abs go-btn" style="left:674px;top:286px">
  <svg width="14" height="14" viewBox="0 0 14 14"><circle cx="8.5" cy="5.5" r="4" fill="#eee" stroke="#555" stroke-width="1.4"/><path d="M5.5 8.5L1.5 12.5" stroke="#444" stroke-width="2.4"/></svg>Go</div>

<section class="abs deals-panel"></section>
<div class="abs h-green" style="left:53px;top:363px">Deals From :</div>
<div class="abs h-green" style="left:180px;top:363px">Deals Result :</div>
<div class="abs count"><b>245</b> Deals, Special Offers from Restaurants</div>

<ul class="abs cat-list">
  <li><span class="box"></span>Beauty Salon</li>
  <li><span class="box"><svg style="position:absolute;left:0;top:-1px" width="10" height="10" viewBox="0 0 10 10"><path d="M1.5 5l2.5 2.5L9 1" stroke="#333" stroke-width="1.5" fill="none"/></svg></span>Restaurant</li>
  <li><span class="box"></span>Cafe</li>
  <li><span class="box"></span>Sports</li>
  <li><span class="box"></span>Shjopping</li>
  <li><span class="box"></span>Hotels</li>
  <li><span class="box"></span>Services</li>
  <li><span class="box"></span>Sensations</li>
  <li><span class="box"></span>Autres</li>
  <li><span class="box"></span>Auto Motives</li>
  <li><span class="box"></span>Events</li>
</ul>

<div class="abs results"></div>
<div class="abs pointer"></div>

<article class="deal-card" style="top:403px">
  <h3 class="deal-title" style="font-weight:400">Tullio are also reproduced in their exact original form, accompanied by English.</h3>
  <div class="deal-photo" role="img" aria-label="Restaurant dining room with set tables" style="background:linear-gradient(135deg,#6b3a26,#a5704e 50%,#3b2418)"></div>
  <p class="deal-text">There are many variations of passages of Lorem Ipsum available, but the majority have suffered in some form, by injected humour. <a>View more</a></p>
  <p class="deal-address"><b>Address :</b> English versions from the 1914 <span>translation by H. Rackmoor.</span></p>
  <div class="price-box">
    <div class="price">$ 32 <em>insted of $ 51</em></div>
    <div class="price-band">This Deal Availabel for <span class="days">2 Days</span></div>
    <div class="btn-more">View more</div>
    <div class="btn-buy">Buy This Deal</div>
  </div>
</article>

<article class="deal-card" style="top:558px">
  <h3 class="deal-title" style="font-weight:400">Tullio are also reproduced in their exact original form, accompanied by English.</h3>
  <div class="deal-photo" role="img" aria-label="Restaurant interior with warm wall panels" style="background:linear-gradient(135deg,#4a3220,#c99a52 45%,#e8dccb 80%)"></div>
  <p class="deal-text">There are many variations of passages of Lorem Ipsum available, but the majority have suffered in some form, by injected humour. <a>View more</a></p>
  <p class="deal-address"><b>Address :</b> English versions from the 1914 <span>translation by H. Rackmoor.</span></p>
  <div class="price-box">
    <div class="price">$ 32 <em>insted of $ 51</em></div>
    <div class="price-band"><span class="num">15</span><span class="unit">Hours</span><span class="num">24</span><span class="unit">mints</span><span class="num">57</span><span class="unit">Secs</span></div>
    <div class="btn-more">View more</div>
    <div class="btn-buy">Buy This Deal</div>
  </div>
</article>

<article class="deal-card" style="top:713px">
  <h3 class="deal-title" style="font-weight:400">Tullio are also reproduced in their exact original form, accompanied by English.</h3>
  <div class="deal-photo" role="img" aria-label="Lounge bar with warm lighting" style="background:linear-gradient(135deg,#2a1a10,#8a5a2c 50%,#d8a560 75%,#2a1a10)"></div>
  <p class="deal-text">There are many variations of passages of Lorem Ipsum available, but the majority have suffered in some form, by injected humour. <a>View more</a></p>
  <p class="deal-address"><b>Address :</b> English versions from the 1914 <span>translation by H. Rackmoor.</span></p>
  <div class="price-box">
    <div class="price">$ 32 <em>insted of $ 51</em></div>
    <div class="price-band">This Deal Availabel for <span class="days">2 Days</span></div>
    <div class="btn-more">View more</div>
    <div class="btn-buy">Buy This Deal</div>
  </div>
</article>

<nav class="abs quick-links">
  <span style="left:51px">Daily Deals</span>
  <span style="left:146px">Hotel Deals</span>
  <span style="left:249px">Restaurant Coupons</span>
  <span style="left:409px">Grocery Coupons</span>
  <span style="left:547px">Printable Coupons</span>
  <span style="left:694px">Shopping Deals</span>
</nav>

<footer class="abs site-footer">
  <div class="f-head" style="left:33px">Find Deals by City :</div>
  <div class="f-head" style="left:435px">more deals</div>
  <ul class="f-col" style="left:46px"><li>Atlanta deals</li><li>Austin deals</li><li>Baltimore deals</li><li>Boston deals</li><li>Charleston deals</li><li>Charlotte deals</li><li>Chicago deals</li></ul>
  <ul class="f-col" style="left:157px"><li>Dallas deals</li><li>Denver deals</li><li>Fort Lauderdale deals</li><li>Fort Worth deals</li><li>Houston deals</li><li>Las Vegas deals</li><li>Los Angeles deals</li></ul>
  <ul class="f-col" style="left:277px"><li>Memphis deals</li><li>Miami deals</li><li>New Orleans deals</li><li>New York deals</li><li>Orlando deals</li><li>Philadelphia deals</li><li>Phoenix deals</li></ul>
  <ul class="f-col" style="left:397px"><li>Richmond deals</li><li>San Diego deals</li><li>San Francisco deals</li><li>San Jose deals</li><li>Seattle deals</li><li>Ventura deals</li><li>Washington deals</li></ul>
  <div class="abs f-sep"></div>
  <div class="f-head" style="left:541px">Find deals by Brand:</div>
  <div class="f-head" style="left:720px">more deals</div>
  <ul class="f-col" style="left:551px"><li>Tinytots Hub</li><li>Linen &amp; Lather</li><li>Voltmart</li><li>Grill Baron</li><li>Threadline</li><li>Hammerhouse</li><li>Flatpakk</li></ul>
  <ul class="f-col" style="left:678px"><li>Deskworks</li><li>Harbor Denim</li><li>Crustly</li><li>Slice Cabin</li><li>Paperclip Co</li><li>Brewhaven</li><li>Longroll</li></ul>
</footer>

<div class="abs bottom-bar">
  <div class="abs" style="left:34px;top:28px">Copyright © 2012 www.duoglimmer.com &nbsp;&nbsp; All rights reserved</div>
  <div class="abs" style="left:576px;top:28px">Connect with</div>
</div>
<div class="social" style="left:626px;background:#3b5998"></div>
<div class="social" style="left:659px;background:#4aa3df"></div>
<div class="social" style="left:692px;background:#e8682a"></div>
<div class="social" style="left:724px;background:#1c6fa8"></div>
<div class="social" style="left:756px;background:#6b8e3a"></div>

</body>
</html>
```